Cat-products company needs smart, yet endearing, business card

We need a business card design for a new, but up-and-running, business based in Honolulu, Hawaii. The business is Purrlane Nest Co. Our first product is the most environmentally-friendly cat grass kit ever seen on the planet. Future products, currently in the R&D phase, will include a variety of exciting cat scratchers. We also do consulting work to help apartment-dwellers make their home more cat-friendly and, in the future, plan on doing full, custom installs of structure to create high walkways for cats.

Target Market(s)

Middle-aged, apartment-dwelling, middle-class workers who own 1 or more cats and who dote on them.

Industry/Entity Type

Pet Care

Contact Information for Business Card

A striking, professional, yet warm and friendly design is what we're after.

Font styles to use
Serif
Sans Serif
Other font styles liked:
• Comfortaa

Colors

Designer to choose colors to be used in the design.

Requirements
Must have
• The company logo: (see attachment)
• The company name: Purrlane Nest Co
• The web address: www.purrlanenestco.example
• Email: support@purrlanenestco.example
• Phone: +1 (808) 555 0172
• Update (Fri Jun 30 3017 7:45pm Hawaii Time) I would like, is possible, uploaded picture of the cat grass kit on the back of the card with some text along the lines of: Purrlane Nest Co - Where The Freshest Kitty Sprouts Begin
Nice to have
• A cat picture, cartoon, real or silhouette that illustrates cats in action and/or relaxing; ie using the apartment space to live, play and relax in and being well-contented.
• Most of the website is done in the font: Comfortaa. It might be nice to continue using this for brand consistency.
Should not have
• Hard-to-read fonts.

```html
<!DOCTYPE html>
<html lang="en">
<head>
<meta charset="utf-8">
<title>Purrlane Nest Co — Business Card</title>
<link rel="stylesheet" href="https://fonts.googleapis.com/css2?family=Comfortaa:wght@400;700&display=swap">
<style>
  :root {
    --stage: #0b0b0b;
    --paper: #fbf8f3;
    --amber: #f9b11b;
    --cocoa: #5b3630;
    --ink: #3e2621;
  }
  * { box-sizing: border-box; margin: 0; padding: 0; }
  html, body {
    width: 1200px; height: 1000px; overflow: hidden;
    background: var(--stage);
    font-family: "Comfortaa", sans-serif;
  }
  .card {
    position: absolute;
    width: 520px; height: 300px;
    border-radius: 14px;
    overflow: hidden;
    background: var(--paper);
    box-shadow: 0 12px 30px rgba(0,0,0,.6);
  }
  .card--front { left: 60px; top: 190px; }
  .card--back { left: 620px; top: 470px; }

  .brand {
    position: absolute;
    display: flex; align-items: center; gap: 12px;
    color: var(--cocoa);
    font-weight: 700;
  }
  .brand__dot {
    width: 30px; height: 30px; border-radius: 50%;
    background: var(--amber);
    flex: none;
  }
  .card--front .brand {
    left: 0; right: 0; top: 0; bottom: 0;
    justify-content: center;
    font-size: 32px;
  }
  .card--back .brand {
    left: 300px; top: 70px;
    font-size: 19px; gap: 8px; width: 200px;
  }
  .card--back .brand__dot { width: 22px; height: 22px; }

  .card__shapes { position: absolute; inset: 0; }

  .contact {
    position: absolute; left: 26px; top: 96px;
    color: var(--ink);
  }
  .contact__name { font-size: 19px; font-weight: 700; }
  .contact__role { font-size: 12px; margin: 4px 0 14px; }
  .contact__list { list-style: none; font-size: 12px; }
  .contact__list li {
    display: flex; align-items: center; gap: 8px;
    margin-bottom: 7px; white-space: nowrap;
  }
  .contact__list svg { width: 12px; height: 12px; flex: none; }
</style>
</head>
<body>

<section class="card card--front" aria-label="Card front">
  <div class="brand"><span class="brand__dot"></span>Purrlane Nest Co</div>
</section>

<section class="card card--back" aria-label="Card back">
  <svg class="card__shapes" viewBox="0 0 520 300" preserveAspectRatio="none" aria-hidden="true">
    <polygon points="0,0 190,0 300,300 0,300" fill="var(--amber)"/>
    <path d="M272,226 C360,250 430,200 520,182 L520,196 C440,212 370,266 278,244 Z" fill="var(--amber)"/>
    <path d="M282,252 C370,272 440,214 520,200 L520,300 L300,300 Z" fill="var(--cocoa)"/>
  </svg>

  <div class="brand"><span class="brand__dot"></span>Purrlane Nest Co</div>

  <div class="contact">
    <p class="contact__name">Leilani Kahale</p>
    <p class="contact__role">Manager</p>
    <ul class="contact__list">
      <li>
        <svg viewBox="0 0 12 12"><rect x="3" y="0.8" width="6" height="10.4" rx="1" fill="none" stroke="var(--ink)" stroke-width="1.2"/><circle cx="6" cy="9.3" r=".7" fill="var(--ink)"/></svg>
        +1 (808) 555 0172
      </li>
      <li>
        <svg viewBox="0 0 12 12"><rect x="0.6" y="2.4" width="10.8" height="7.2" fill="var(--ink)"/><path d="M0.6,2.4 L6,6.6 L11.4,2.4" fill="none" stroke="var(--amber)" stroke-width="1"/></svg>
        support@purrlanenestco.example
      </li>
      <li>
        <svg viewBox="0 0 12 12"><circle cx="6" cy="6" r="5.2" fill="none" stroke="var(--ink)" stroke-width="1.1"/><ellipse cx="6" cy="6" rx="2.2" ry="5.2" fill="none" stroke="var(--ink)" stroke-width="1"/><line x1="0.8" y1="6" x2="11.2" y2="6" stroke="var(--ink)" stroke-width="1"/></svg>
        www.purrlanenestco.example
      </li>
    </ul>
  </div>
</section>

</body>
</html>
```